Bookcover: Lessons From the Silent Orchard

I am publishing a super-low-cost innovation book for €4,99 on Bravolo Self Release to help everyone become a great innovator: young ambitious people without college education nor a big budget. Do you want to help me?

Brief:
Design a book cover 1600 x 2560 pixels for BSR.
Main title: Lessons From the Silent Orchard
Sub title: mindset - insights - skills & tools
Author: Maarten de Klerk
Design: captive, and appealing to everyone
Target Group: young ambitious people without college education

For bravolo please format the height/width ratio of 1.6:1

```html
<!DOCTYPE html>
<html lang="en">
<head>
<meta charset="utf-8">
<title>Lessons From the Silent Orchard – Book Cover</title>
<link rel="stylesheet" href="https://fonts.googleapis.com/css2?family=Lilita+One&display=swap">
<style>
  :root {
    --page-bg: #f3f8fd;
    --cover-blue: #3a5f86;
    --cover-blue-light: #6f86a3;
    --cream: #fdf5e8;
    --amber: #f6ac28;
    --amber-glow: #f7b54a;
  }
  * { box-sizing: border-box; margin: 0; padding: 0; }
  html, body {
    width: 859px;
    height: 1200px;
    overflow: hidden;
    background: var(--page-bg);
  }
  .book-cover {
    position: absolute;
    left: 121px;
    top: 105px;
    width: 618px;
    height: 989px;
    background: var(--cover-blue);
    color: var(--cream);
    font-family: "Lilita One", sans-serif;
    text-align: center;
  }
  .title {
    position: absolute;
    top: 68px;
    left: 0;
    width: 100%;
    font-size: 62px;
    line-height: 74px;
    font-weight: 400;
    letter-spacing: 0.5px;
  }
  .title span { display: block; }
  .hero-art {
    position: absolute;
    left: 110px;
    top: 300px;
    width: 398px;
    height: 380px;
    border-radius: 50%;
    background: radial-gradient(circle at 50% 48%,
      var(--amber) 0%, var(--amber-glow) 28%,
      var(--cover-blue-light) 45%, var(--cover-blue) 70%);
  }
  .subtitle {
    position: absolute;
    top: 705px;
    left: 0;
    width: 100%;
    list-style: none;
    font-size: 31px;
    line-height: 42px;
  }
  .subtitle li {
    display: flex;
    justify-content: center;
    align-items: center;
    gap: 34px;
  }
  .rule {
    display: block;
    width: 42px;
    height: 3px;
    background: var(--amber);
    position: relative;
  }
  .rule::after {
    content: "";
    position: absolute;
    top: -2px;
    width: 7px;
    height: 7px;
    border-radius: 50%;
    background: var(--amber);
  }
  .rule--left::after { left: -2px; }
  .rule--right::after { right: -2px; }
  .author {
    position: absolute;
    top: 910px;
    left: 0;
    width: 100%;
    font-size: 26px;
    letter-spacing: 0.5px;
  }
</style>
</head>
<body>
  <main class="book-cover">
    <h1 class="title">
      <span>Lessons From</span>
      <span>the Silent</span>
      <span>Orchard</span>
    </h1>

    <div class="hero-art" role="img" aria-label="Illustration of a glowing yellow light bulb with radiating rays"></div>

    <ul class="subtitle">
      <li><span class="rule rule--left"></span>MINDSET<span class="rule rule--right"></span></li>
      <li><span class="rule rule--left"></span>INSIGHTS<span class="rule rule--right"></span></li>
      <li><span class="rule rule--left"></span>SKILLS &amp;<span class="rule rule--right"></span></li>
      <li>TOOLS</li>
    </ul>

    <p class="author">MAARTEN DE KLERK</p>
  </main>
</body>
</html>
```